Business Card Design Project

Recently had a new logo made up for my company and new business cards done as well. I have attached the logos for your viewing. Additional projects may be needed. Good luck!

Industry/Entity Type

Business

```html
<!DOCTYPE html>
<html lang="en">
<head>
<meta charset="utf-8">
<title>Business Card – Front and Back</title>
<link rel="stylesheet" href="https://fonts.googleapis.com/css2?family=Tinos:ital,wght@1,700&display=swap">
<style>
  :root {
    --page: #ffffff;
    --card-dark: #302e2f;
    --card-edge: #1f1d1e;
    --lime: #a1bd3b;
    --olive: #8a9b25;
    --pale-lime: #cfdc8c;
    --name-green: #8fc33a;
    --title-gold: #e2bd2c;
    --phone-red: #d5232a;
    --text-white: #ffffff;
    --text-black: #111111;
  }
  html, body {
    margin: 0;
    padding: 0;
    overflow: hidden;
    background: var(--page);
  }
  .canvas {
    width: 848px;
    height: 1200px;
    overflow: hidden;
    background: var(--page);
  }
  .canvas svg { display: block; width: 848px; height: 1200px; }
  .card-text {
    font-family: "Tinos", "Times New Roman", serif;
    font-style: italic;
    font-weight: 700;
  }
  .card-body { fill: var(--card-dark); }
  .card-edge { fill: var(--card-edge); }
  .band-lime { fill: var(--lime); }
  .band-olive { fill: var(--olive); }
  .band-pale { fill: var(--pale-lime); }
  .person-name { fill: var(--name-green); font-size: 34px; }
  .person-title { fill: var(--title-gold); font-size: 20px; }
  .contact-phone { fill: var(--phone-red); font-size: 21px; }
  .contact-company { fill: var(--text-white); font-size: 16px; }
  .contact-email { fill: var(--text-black); font-size: 16px; }
</style>
</head>
<body>
<main class="canvas">
  <svg viewBox="0 0 600 848" xmlns="http://www.w3.org/2000/svg">
    <!-- Back card: contact side -->
    <g class="card card-back">
      <polygon class="card-edge" points="60,268 511,198 550,451 98,521"/>
      <polygon class="card-body" points="60,268 511,198 548,448 97,518"/>
      <polygon class="band-olive" points="76,382 293,352 295,372 78,400"/>
      <polygon class="band-pale" points="80,406 297,378 299,398 82,426"/>
      <polygon class="band-pale" points="86,432 302,405 304,425 88,453"/>
      <polygon class="band-lime" points="90,472 545,405 548,448 97,518"/>
      <text class="card-text contact-phone" x="378" y="337">9800123456</text>
      <text class="card-text contact-company" x="382" y="386">BRIGHTPATH CO.</text>
      <text class="card-text contact-email" x="115" y="483">RAVEN2718@MAILBOX.COM</text>
    </g>

    <!-- Front card: name side -->
    <g class="card card-front">
      <polygon class="card-body" points="60,120 500,0 575,210 108,265"/>
      <polygon class="band-lime" points="290,65 500,0 505,15 295,80"/>
      <polygon class="band-lime" points="400,50 508,17 511,31 403,66"/>
      <polygon class="band-lime" points="112,268 218,234 221,250 115,283"/>
      <polygon class="band-lime" points="120,295 332,226 335,245 124,314"/>
      <polygon class="band-lime" points="133,330 568,183 575,210 140,357"/>
      <text class="card-text person-name" x="176" y="150">RAVEN HOLLOWAY</text>
      <text class="card-text person-title" x="272" y="175">MANAGER</text>
    </g>
  </svg>
</main>
</body>
</html>
```